Creative Business Card

Were looking for a new fresh and creative look to our Business card. Our company name is InkVale. Be creative, Were attaching our logo and our base colors, but your free to do anything. Name, title, Phone

Industry/Entity Type

Business

```html
<!DOCTYPE html>
<html lang="en">
<head>
<meta charset="utf-8">
<title>InkVale Business Card</title>
<link href="https://fonts.googleapis.com/css2?family=Open+Sans:wght@400;700;800&display=swap" rel="stylesheet">
<style>
  :root {
    --backdrop: #c9c9c9;
    --card-white: #ffffff;
    --card-dark: #2b2d2f;
    --card-dark-deep: #202224;
    --brand-green: #7dc242;
    --brand-blue: #0a6fc2;
    --text-light: #f2f2f2;
    --text-muted: #d0d0d0;
  }
  * { box-sizing: border-box; margin: 0; padding: 0; }
  html, body {
    width: 1200px; height: 900px; overflow: hidden;
    background: var(--backdrop);
    font-family: "Open Sans", Arial, sans-serif;
  }
  .stage {
    position: relative; width: 1200px; height: 900px;
    display: flex; align-items: center; justify-content: center; gap: 60px;
  }
  .card {
    position: relative; width: 500px; height: 286px;
    border-radius: 20px; overflow: hidden;
  }
  /* Front */
  .card-front { background: var(--card-dark); }
  .front-header {
    height: 128px; background: var(--card-white);
    display: flex; align-items: center; padding-left: 24px;
  }
  .brand-name {
    font-weight: 800; color: var(--brand-green);
    letter-spacing: 1px; line-height: 1;
  }
  .front-header .brand-name { font-size: 62px; }
  .accent-stripe { height: 8px; background: var(--brand-blue); }
  .front-body { padding: 12px 24px 0; }
  .person-name { font-size: 17px; font-weight: 700; color: var(--brand-green); line-height: 1.2; }
  .person-title { font-size: 11px; color: var(--text-muted); margin-bottom: 16px; }
  .contact-list { list-style: none; }
  .contact-item {
    display: flex; align-items: center; gap: 6px;
    font-size: 14px; color: var(--text-light); line-height: 20px;
  }
  .contact-icon { width: 13px; height: 13px; flex: none; }
  /* Back */
  .card-back {
    background: radial-gradient(ellipse at 55% 45%, #34373a 0%, var(--card-dark) 45%, var(--card-dark-deep) 100%);
    display: flex; align-items: center; justify-content: center;
  }
  .card-back .brand-name { font-size: 64px; }
</style>
</head>
<body>
<main class="stage">
  <section class="card card-front" aria-label="Business card front">
    <header class="front-header">
      <span class="brand-name">InkVale</span>
    </header>
    <div class="accent-stripe"></div>
    <div class="front-body">
      <p class="person-name">Dana Reyes</p>
      <p class="person-title">Manager</p>
      <ul class="contact-list">
        <li class="contact-item">
          <svg class="contact-icon" viewBox="0 0 16 16"><path fill="#7dc242" d="M3.5 1l3 3-1.7 1.7c.8 1.8 2.2 3.2 4 4L10.5 8l3 3-1.8 2.4C7 13 3 9 2.6 3z"/></svg>
          (916) 555-0142
        </li>
        <li class="contact-item">
          <svg class="contact-icon" viewBox="0 0 16 16"><rect x="1" y="3.5" width="14" height="10" rx="1" fill="#7dc242"/><path d="M1.5 4.5L8 9.5l6.5-5" fill="none" stroke="#2b2d2f" stroke-width="1.4"/></svg>
          dana@inkvale.com
        </li>
        <li class="contact-item">
          <svg class="contact-icon" viewBox="0 0 16 16"><g fill="none" stroke="#7dc242" stroke-width="1.5"><circle cx="8" cy="8" r="6.5"/><ellipse cx="8" cy="8" rx="3" ry="6.5"/><path d="M1.5 8h13"/></g></svg>
          www.inkvale.com
        </li>
        <li class="contact-item">
          <svg class="contact-icon" viewBox="0 0 16 16"><path fill="#7dc242" d="M8 1.5L1 8h2v6.5h4v-4h2v4h4V8h2z"/></svg>
          2140 Cedar Hollow Road, Suite D
        </li>
      </ul>
    </div>
  </section>

  <section class="card card-back" aria-label="Business card back">
    <span class="brand-name">InkVale</span>
  </section>
</main>
</body>
</html>
```